business card and letter head for Australian company manufacturing rienforcing steel for constructio

business card and letter head using our logo. you will need to change the name of the logo to SOLVAKIT and the red part of the logo needs to start at the e after d.

Target Market(s)

Architects, Engineers, Builders, Developers

Industry/Entity Type

Manufacturing

```html
<!DOCTYPE html>
<html lang="en">
<head>
<meta charset="utf-8">
<title>Solvakit Letterhead</title>
<link rel="stylesheet" href="https://fonts.googleapis.com/css2?family=Arimo:wght@400;700&display=swap">
<style>
  :root {
    --brand-green: #8bbf41;
    --brand-green-dark: #6f9c34;
    --brand-red: #a3262d;
    --ink-dark: #3d3d3c;
    --paper: #ffffff;
    --footer-text: #ffffff;
  }
  * { margin: 0; padding: 0; box-sizing: border-box; }
  html, body {
    width: 927px;
    height: 1200px;
    overflow: hidden;
    background: var(--paper);
  }
  .letterhead {
    position: relative;
    width: 927px;
    height: 1200px;
    background: var(--paper);
    font-family: "Arimo", Arial, sans-serif;
  }
  .letterhead__header {
    position: absolute;
    top: 0;
    left: 0;
    width: 100%;
    height: 126px;
    background: var(--brand-green);
    border-bottom: 7px solid var(--brand-green-dark);
  }
  .brand {
    position: absolute;
    left: 26px;
    top: 16px;
    width: 168px;
    display: flex;
    flex-direction: column;
    align-items: center;
  }
  .brand__mark {
    width: 48px;
    height: 46px;
    background: var(--brand-red);
  }
  .brand__name {
    margin-top: 10px;
    font-size: 29px;
    font-weight: 700;
    letter-spacing: 1px;
    color: var(--ink-dark);
    line-height: 1;
    white-space: nowrap;
  }
  .letterhead__body {
    position: absolute;
    top: 126px;
    left: 0;
    width: 100%;
    height: 1001px;
  }
  .letterhead__footer {
    position: absolute;
    left: 0;
    bottom: 0;
    width: 100%;
    height: 73px;
    background: var(--ink-dark);
    display: flex;
    align-items: center;
    padding-left: 38px;
  }
  .footer__address {
    font-size: 20px;
    font-weight: 400;
    color: var(--footer-text);
    white-space: nowrap;
  }
</style>
</head>
<body>
  <div class="letterhead">
    <header class="letterhead__header">
      <div class="brand">
        <span class="brand__mark"></span>
        <span class="brand__name">SOLVAKIT</span>
      </div>
    </header>
    <main class="letterhead__body"></main>
    <footer class="letterhead__footer">
      <p class="footer__address">Address : Level 14, 52 Harbour Row. North Sydney. Postal Code , Australia.</p>
    </footer>
  </div>
</body>
</html>
```